Premium label design for product needed

UPDATE: (Scroll down)
For a face care product i need a new front label on the bottle. The current one is white and i want to add the franchise color green. The objective is to premiunize the packaging and to give guidance to the consumers to find their franchise color. The task is to find several option to color the label on the bottle in the most premium way. But at the same time it should not be playful, more in a serious medical direction or in a counterbrand direction. It should look absolutely premium. but should not shout to much. The text structure should remain the same. I will provide a powerpoint slide to illustrate the task even clearer.
UPDATE: DO NOT DESIGN THE FOLDING BOX, only design the bottle. The folding box only serves the purpose of giving the text/layout structure and rough color intent.

Target Market(s)

female 25-39

Requirements
Must have
• Premium, Uniqueness, Innovative

```html
<!DOCTYPE html>
<html lang="en">
<head>
<meta charset="utf-8">
<title>Vera Acne Solution – Front Label</title>
<link href="https://fonts.googleapis.com/css2?family=Roboto:wght@300;400;700&display=swap" rel="stylesheet">
<style>
  :root {
    --page-bg: #ffffff;
    --silver-dark: #b9bcc0;
    --silver-mid: #d6d8db;
    --silver-light: #f1f2f3;
    --ink-navy: #141a2e;
    --ink-grey: #2a2f3a;
    --franchise-green: #5fae7f;
    --franchise-green-soft: #8fcaa3;
    --accent-burgundy: #6e0f1c;
  }
  html, body {
    margin: 0;
    padding: 0;
    width: 1200px;
    height: 1200px;
    overflow: hidden;
    background: var(--page-bg);
  }
  .canvas {
    position: relative;
    width: 1200px;
    height: 1200px;
    font-family: "Roboto", Arial, sans-serif;
  }
  .label {
    position: absolute;
    left: 300px;
    top: 75px;
    width: 600px;
    height: 1050px;
    background: linear-gradient(90deg,
      var(--silver-dark) 0%,
      var(--silver-light) 22%,
      var(--silver-mid) 45%,
      var(--silver-light) 65%,
      var(--silver-dark) 100%);
    overflow: hidden;
  }
  .product-name {
    position: absolute;
    left: 14px;
    top: 72px;
    margin: 0;
    color: var(--ink-navy);
    line-height: 1;
  }
  .product-name .brand-line {
    display: block;
    font-weight: 700;
    font-size: 88px;
    letter-spacing: -1px;
  }
  .product-name .sub-line {
    display: block;
    font-weight: 300;
    font-size: 80px;
    letter-spacing: 1px;
    margin-top: 8px;
  }
  .franchise-stripe {
    position: absolute;
    left: 12px;
    top: 286px;
    width: 584px;
    height: 26px;
    background: linear-gradient(180deg, var(--franchise-green-soft), var(--franchise-green));
  }
  .chevron {
    position: absolute;
    left: 18px;
    top: 346px;
    width: 572px;
    height: 98px;
  }
  .variant {
    position: absolute;
    left: 14px;
    top: 790px;
    margin: 0;
    font-weight: 400;
    font-size: 39px;
    color: var(--ink-grey);
    letter-spacing: 0.5px;
  }
  .claim-band {
    position: absolute;
    left: 6px;
    top: 889px;
    width: 594px;
    height: 78px;
    background: linear-gradient(180deg, var(--franchise-green-soft), var(--franchise-green));
    display: flex;
    align-items: center;
    padding-left: 22px;
    box-sizing: border-box;
  }
  .claim-band p {
    margin: 0;
    font-size: 36px;
    font-weight: 400;
    color: var(--accent-burgundy);
  }
</style>
</head>
<body>
<div class="canvas">
  <div class="label">
    <h1 class="product-name">
      <span class="brand-line">Vera ACNE</span>
      <span class="sub-line">SOLUTION</span>
    </h1>
    <div class="franchise-stripe"></div>
    <svg class="chevron" viewBox="0 0 572 98" preserveAspectRatio="none" aria-hidden="true">
      <polygon points="0,0 572,0 572,31 294,98 0,31" fill="var(--accent-burgundy)"/>
    </svg>
    <p class="variant">A.I. MATT FLUID</p>
    <div class="claim-band">
      <p>Lorem ipsum dolor sit amet,</p>
    </div>
  </div>
</div>
</body>
</html>
```